Crowdsourced Research Platform: KOVAL Polls

KOVAL Polls is an acronym for Kindred Opinion Views Among Lands (KOVAL) Polls. This is a research effort to format and combine multiple sources of public opinion data from around the world into merged datasets. The website will at first mainly act as a quality control hub and distribution point for official dataset releases. It will provide resources such as codebooks, development guidelines, and instructional videos for crowdsourcing continued expansion of the resource. We need a coded (HTML and CSS) website design and associated files to launch the website with ease. We purchased the domain www.kovalpolls.org, but access is blocked while it is under construction.

The website design should be based on a logo recently commissioned (see attached). The design should be simple and professional with lots of white space. We would like the logo on the top left of all pages and the primary navigation menu along the top-right of all pages. The primary navigation menu should have a simple mouse-over effect and the main menu items should expand with secondary drop-down options. The footer should include a few columns with headings and links to different pages. The website layout should be dynamic and expand its width to fit different sized screens. There will be a lot of data and information displayed in tables, so we would like the CSS coding and website design to include tables designed to match the website theme. The main graphical content will be data visualisations such as pie/bar charts, histograms, scatter plots, heat maps, moving average trend lines etc. We would therefore like the design to include modular sections (boxes matching theme to display plots/graphs/etc) that can visually display these types of figures with text/caption underneath to explain the data visualizations.

For more information and written placeholder content, designers should read the attached documents to get a better idea about the project. Some draft working papers using merged datsets have been included for reference and you can use these for their examples of data visualizations and use the written content for filling in page content.

Target Market(s)

The primary target audience will be academics in universities and research institutes. The resource will be most useful to quantitative social scientists, particularly political scientists and sociologists, but any discipline concerned with us humans could find the resource useful. Others such as graduate-level university students, civil servants in government departments, members of research institutions, and policy researchers in non-profit organizations will also find the resource useful.

Coding

Coded - Design and coding required

Number of Pages Required

3 page

Font styles to use
Sans Serif

Colors

Designer to choose colors to be used in the design.

Requirements
Must have
• HTML and CSS coding (not Wordpress)
Nice to have
• Content boxes to display data visualizations alongside articles.

```html
<!DOCTYPE html>
<html lang="en">
<head>
<meta charset="utf-8">
<title>KOVAL Polls</title>
<link rel="stylesheet" href="https://fonts.googleapis.com/css2?family=Montserrat:wght@400;600;700;800&family=Open+Sans:wght@400;600;700&display=swap">
<style>
:root{
  --blue:#1e86d8;
  --blue-dark:#1767bb;
  --blue-light:#2b93e2;
  --ink:#222831;
  --text:#6b7079;
  --muted:#9aa0a8;
  --paper:#ffffff;
  --soft:#f3f4f6;
  --card:#f5f6f8;
  --footer:#22252a;
  --footer-line:#34383e;
}
*{box-sizing:border-box;margin:0;padding:0}
html,body{width:1200px;height:4327px;overflow:hidden}
body{font-family:"Open Sans",Arial,sans-serif;color:var(--text);background:var(--paper);font-size:13px;line-height:1.65}
h1,h2,h3,h4,.brand,.nav a,.btn{font-family:"Montserrat",Arial,sans-serif}
a{text-decoration:none;color:inherit}
.more{display:inline-block;color:var(--blue);font-family:"Montserrat",Arial,sans-serif;font-size:11px;font-weight:700;margin-top:10px;letter-spacing:.3px}
.btn{display:inline-block;font-size:12px;font-weight:700;letter-spacing:.6px;padding:12px 26px;text-transform:uppercase}
.img{display:block}

/* hero */
.hero{position:relative;height:554px;background:linear-gradient(100deg,#4b5662 0%,#707a84 35%,#8d8f8f 60%,#5b5f64 100%);overflow:hidden}
.hero .img{position:absolute;inset:0;background:radial-gradient(ellipse at 78% 55%,rgba(205,180,160,.55),transparent 45%),linear-gradient(180deg,rgba(20,30,45,.35),rgba(20,30,45,.55))}
.topbar{position:absolute;top:0;left:0;right:0;height:72px;display:flex;align-items:center;padding:0 160px;justify-content:space-between}
.brand{display:flex;align-items:center;gap:10px;color:#fff;font-size:21px;font-weight:600}
.brand .dot{width:24px;height:24px;border-radius:50%;border:2px solid var(--blue-light)}
.nav{display:flex;align-items:center;gap:6px}
.nav a{color:#fff;font-size:12px;font-weight:600;padding:8px 11px}
.nav a.active{background:var(--blue)}
.nav .search{width:30px;height:30px;border:1px solid rgba(255,255,255,.6);display:flex;align-items:center;justify-content:center;margin-left:10px}
.slides{position:absolute;left:34px;top:205px;color:#fff;font-family:"Montserrat",Arial,sans-serif}
.slides span{display:block;font-size:12px;opacity:.45;margin:8px 0}
.slides strong{display:block;font-size:26px;font-weight:700}
.hero-copy{position:absolute;top:198px;left:0;right:0;text-align:center;color:#fff}
.hero-copy h1{font-size:37px;line-height:1.15;font-weight:400;text-transform:uppercase}
.hero-copy h1 b{font-weight:800}
.hero-copy .btn{background:var(--blue);color:#fff;margin-top:28px;padding:13px 28px}

/* feature grid */
.features{display:grid;grid-template-columns:repeat(3,400px);grid-template-rows:repeat(3,301px);height:903px}
.tile{padding:44px 34px 0 34px;background:var(--paper)}
.tile h2{color:var(--ink);font-size:20px;font-weight:700;text-transform:uppercase;margin-bottom:12px}
.tile p{font-size:11.5px;line-height:1.7;color:var(--muted)}
.tile.about{padding-top:60px}
.ph-woman{grid-column:1;grid-row:1/3;background:linear-gradient(160deg,#eae7e2,#c9b8a6 55%,#8c7a6a)}
.ph-desk{grid-column:2;grid-row:1;background:linear-gradient(135deg,#f4f4f4,#d9dadc 50%,#9fa3a8)}
.ph-board{grid-column:3;grid-row:2;background:linear-gradient(135deg,#eef0f2,#c7ccd2 50%,#7f8790)}
.ph-meeting{grid-column:2;grid-row:3;background:linear-gradient(135deg,#e9ebee,#b8bec6 50%,#6f7a86)}

/* vocabulary */
.vocab{height:346px;background:var(--blue);color:#fff;text-align:center;padding-top:62px}
.vocab h2{font-size:30px;font-weight:800;letter-spacing:1px;margin-bottom:18px}
.vocab p{width:900px;margin:0 auto 10px;font-size:13px;line-height:1.65;color:#eaf3fc}
.vocab .btn{background:#fff;color:var(--blue);margin-top:16px;padding:10px 22px;font-size:11px}

/* sources */
.sources{height:491px;background:var(--soft);display:flex;padding:42px 0 42px 0}
.ph-team{width:600px;height:407px;background:linear-gradient(120deg,#e7e9ec,#c5c9cf 45%,#8a8f95)}
.sources-copy{padding:14px 40px 0 40px;width:600px}
.sources-copy h2{color:var(--blue);font-size:30px;font-weight:800;margin-bottom:10px}
.sources-copy p{font-size:12.5px;margin-bottom:18px}
.src-list{list-style:none;columns:2;column-gap:30px;font-size:10.5px;line-height:2.05;color:var(--text)}
.src-list li{padding-left:14px;position:relative}
.src-list li::before{content:"";position:absolute;left:2px;top:9px;width:5px;height:5px;background:var(--blue);border-radius:50%}

/* articles */
.articles{height:1197px;padding:50px 18px 0}
.articles h2{text-align:center;color:var(--blue);font-size:31px;font-weight:800;margin-bottom:34px}
.article-grid{display:grid;grid-template-columns:repeat(4,1fr);column-gap:20px;row-gap:22px}
.card{background:var(--card)}
.card .img{height:346px}
.row2 .img{height:337px}
.card .body{padding:20px 18px 22px}
.card .meta{font-size:10px;color:var(--muted)}
.card h3{color:var(--ink);font-size:17px;font-weight:700;text-transform:uppercase;margin:6px 0 8px;line-height:1.25}
.card p{font-size:11px;line-height:1.6;color:var(--muted)}
.card.wide{grid-column:span 2}
.g1{background:linear-gradient(150deg,#eef0f3,#c3c8cf 55%,#8d949d)}
.g2{background:linear-gradient(150deg,#f2f2f3,#d6d7da 55%,#a2a5aa)}
.g3{background:linear-gradient(150deg,#e6e9ed,#b4bcc6 55%,#6f7b89)}
.g4{background:linear-gradient(150deg,#e5e6e8,#b7b9bd 55%,#5f6368)}

/* highlight panels */
.panels{height:404px;display:flex}
.panel{width:600px;color:#fff;padding:64px 50px 0}
.panel.left{background:var(--blue-dark)}
.panel.right{background:var(--blue-light)}
.panel h2{font-size:24px;font-weight:800;letter-spacing:.8px;margin-bottom:16px;text-transform:uppercase}
.panel p{font-size:13.5px;line-height:1.65;color:#e8f2fb}
.panel .btn{background:#fff;color:var(--blue-dark);margin-top:28px;padding:10px 22px;font-size:11px}

/* footer */
.footer{height:432px;background:var(--footer);color:#b7bbc1;text-align:center;position:relative}
.footer .brand{justify-content:center;padding-top:58px;font-size:30px}
.footer .brand .dot{width:32px;height:32px}
.footer .about{width:860px;margin:24px auto 0;font-size:11.5px;line-height:1.6}
.subscribe{display:flex;justify-content:center;margin-top:22px}
.subscribe .field{width:380px;height:40px;background:#fff;text-align:left;padding:10px 14px;color:#a5a9ae;font-size:12px}
.subscribe .btn{background:var(--blue);color:#fff;padding:0 34px;line-height:40px}
.foot-nav{display:flex;justify-content:center;gap:30px;margin-top:28px}
.foot-nav a{color:#fff;font-family:"Montserrat",Arial,sans-serif;font-size:12px;font-weight:700}
.legal{position:absolute;left:0;right:0;bottom:0;height:86px;border-top:1px solid var(--footer-line);display:flex;justify-content:space-between;align-items:center;padding:0 40px}
.legal p{font-size:11px;text-align:left}
.legal p b{color:#fff}
.social{display:flex;gap:10px}
.social span{width:28px;height:28px;border-radius:50%;background:#d8dadd}
</style>
</head>
<body>

<header class="hero">
  <div class="img" role="img" aria-label="Photo of a smiling woman in a bright office"></div>
  <div class="topbar">
    <a class="brand" href="#"><span class="dot"></span>KOVAL Polls</a>
    <nav class="nav">
      <a class="active" href="#">Home</a>
      <a href="#">About us</a>
      <a href="#">Services</a>
      <a href="#">Testimonials</a>
      <a href="#">Blog</a>
      <a href="#">Contact us</a>
      <span class="search"><svg width="13" height="13" viewBox="0 0 14 14"><circle cx="6" cy="6" r="4.5" fill="none" stroke="#fff" stroke-width="1.6"/><line x1="9.3" y1="9.3" x2="13" y2="13" stroke="#fff" stroke-width="1.6"/></svg></span>
    </nav>
  </div>
  <div class="slides"><span>01</span><strong>02</strong><span>03</span></div>
  <div class="hero-copy">
    <h1><b>KOVAL Polls</b> make it &nbsp;easier<br>to work <b>with multiple sources</b><br><b>of public</b></h1>
    <a class="btn" href="#">Latest surveys</a>
  </div>
</header>

<section class="features">
  <div class="ph-woman img" role="img" aria-label="Photo of a woman at a desk with a coffee cup"></div>
  <div class="ph-desk img" role="img" aria-label="Photo of a desk with documents, glasses and a pen"></div>
  <article class="tile">
    <h2>Country-survey</h2>
    <p>Country-survey data is aggregated respondent data that draws on the structure of many different surveys. Each observation represents many people within each country within each survey round. This data is ideal for linking aggregated indicators between different survey sources, especially when they overlap in the same countries in the same years.</p>
    <a class="more" href="#">+ READ MORE</a>
  </article>
  <article class="tile">
    <h2>Respondent</h2>
    <p>Respondent data is composed of individual items used by people in a survey round. Each observation is a person who responded to questions about opinion and national issues. This dataset is ideal for exploring differences between groups of people or any research question dealing with the individual level. Respondent data includes harmonised demographic indicators as well as a set of merged attitude variables from the sources listed.</p>
    <a class="more" href="#">+ READ MORE</a>
  </article>
  <div class="ph-board img" role="img" aria-label="Photo of a presenter at a whiteboard with charts"></div>
  <article class="tile about">
    <h2>About us</h2>
    <p>KOVAL Polls make it easier to work with multiple sources of public opinion data. It does so by formatting variables for consistency and merging datasets together. The current merged dataset includes millions of respondents, covers most countries in the world, and extends back several decades. This increased variation improves the research questions that can be addressed with confidence.</p>
    <a class="more" href="#">+ READ MORE</a>
  </article>
  <div class="ph-meeting img" role="img" aria-label="Photo of colleagues in a meeting room"></div>
  <article class="tile">
    <h2>Country-year</h2>
    <p>Country-year data refers to country-level data that is aggregated, but it is no longer meaningful to distinguish between different survey sources. Each observation represents mean scores within the same country and year for some key variables taken from multiple survey sources. This data is designed to be merged into other country-year datasets.</p>
    <a class="more" href="#">+ READ MORE</a>
  </article>
</section>

<section class="vocab">
  <h2>VOCABULARY</h2>
  <p>The following terms and phrases have specific meanings in relation to KOVAL Polls. Here "survey" refers to a randomized sample of the adult population of a country and are thus designed to be nationally representative of the public. Some surveys are included if they focus on particular groups such as youth or the unemployed, but these are noted as special surveys. Surveys are usually conducted in person, but they may also be done over the phone, by mail, or online.</p>
  <p>Individuals being surveyed or interviewed are often referred to as a "respondent" and their answers are often referred to as "responses". Respondents are asked a set of questions, or "survey items", and their responses measure public opinion.</p>
  <a class="btn" href="#">Read more</a>
</section>

<section class="sources">
  <div class="ph-team img" role="img" aria-label="Photo of two researchers reviewing work on a laptop"></div>
  <div class="sources-copy">
    <h2>SOURCES AND YEARS</h2>
    <p>KOVAL Polls merges data from nineteen different survey sources. These are displayed below together with the range of years covered by each source.</p>
    <ul class="src-list">
      <li>Meridian Barometer (1999-2015)</li>
      <li>Dune Barometer: Cycles I to IV (2006-2016)</li>
      <li>Lotus Barometer (2001-2016)</li>
      <li>Eastgate Barometer (1991-2004)</li>
      <li>Highland Barometer (2008-2013)</li>
      <li>Cordillera Monitor (1995-2015)</li>
      <li>Continental Pulse: Standard Series (1973-2016)</li>
      <li>Northfield Social Survey (2002-2014)</li>
      <li>Harbor Opinion Tracker (2002-2015)</li>
      <li>Intercountry Attitudes Programme (1985-2014)</li>
      <li>Pacific Survey of Values (2003-2015)</li>
      <li>Comparative Ballot Panel (1996-2016)</li>
      <li>Global Outlook Study (1981-2014)</li>
      <li>Youth Voices Survey (2001-2014)</li>
      <li>Civic Trust Barometer (1995-2016)</li>
      <li>Continental Pulse: Candidate Countries (1990-2004)</li>
      <li>Continental Pulse: Special Series (1974-2016)</li>
      <li>Southern Cone Survey (2004-2014)</li>
      <li>Island Nations Poll (2006-2015)</li>
      <li>Great Lakes Survey (2002-2016)</li>
    </ul>
  </div>
</section>

<section class="articles">
  <h2>MOST READ ARTICAL KOVAL POLLS</h2>
  <div class="article-grid">
    <article class="card">
      <div class="img g1" role="img" aria-label="Photo of a hand pointing at a chart on a flipboard"></div>
      <div class="body">
        <span class="meta">28 Jan 2016 / Comment 2</span>
        <h3>File structure</h3>
        <p>You can setup your KOVAL Polls directory anywhere on your hard drive, but the folders and subfolders within this directory must match those referred to in the scripts. Avoid changing folder names so files stay accessible and scripts run smoothly.</p>
        <a class="more" href="#">+ READ MORE</a>
      </div>
    </article>
    <article class="card">
      <div class="img g2" role="img" aria-label="Photo of hands reviewing printed reports with a pen"></div>
      <div class="body">
        <span class="meta">28 Jan 2016 / Comment 2</span>
        <h3>Define main folder</h3>
        <p>You will need to update the reference to the main directory at the top of the script called "Create Dataset". What you enter here will depend on where you placed the folder on your hard drive.</p>
        <a class="more" href="#">+ READ MORE</a>
      </div>
    </article>
    <article class="card">
      <div class="img g3" role="img" aria-label="Photo of a team gathered around a presenter"></div>
      <div class="body">
        <span class="meta">28 Jan 2016 / Comment 2</span>
        <h3>Run the scripts</h3>
        <p>Three scripts create three datasets at three levels of analysis and must be run in the correct order. Run the script titled "Respondent Data" first, then the country-survey and country-year scripts.</p>
        <a class="more" href="#">+ READ MORE</a>
      </div>
    </article>
    <article class="card">
      <div class="img g4" role="img" aria-label="Photo of a person typing on a laptop at a desk"></div>
      <div class="body">
        <span class="meta">28 Jan 2016 / Comment 2</span>
        <h3>Adding sources and variables</h3>
        <p>There are several ways of adding variables and sources to future releases of KOVAL Polls. Our preference is that you update the scripts and send them to us for review.</p>
        <a class="more" href="#">+ READ MORE</a>
      </div>
    </article>

    <article class="card wide row2">
      <div class="img g3" role="img" aria-label="Photo of three colleagues smiling around a laptop"></div>
      <div class="body">
        <span class="meta">28 Jan 2016 / Comment 2</span>
        <h3>Download source datasets</h3>
        <p>We cannot provide the original datasets because many sources require prior registration and agreement to their usage terms before downloading. Please visit each source to download the necessary files, keeping the original file names where available, and place them in the appropriate subfolder within the source datasets folder.</p>
        <a class="more" href="#">+ READ MORE</a>
      </div>
    </article>
    <article class="card row2">
      <div class="img g1" role="img" aria-label="Photo of a business team in discussion"></div>
      <div class="body">
        <span class="meta">28 Jan 2016 / Comment 2</span>
        <h3>Social trust</h3>
        <p>At the respondent level, the common variable distinguishes between individuals who generally trust most people and those that would be more careful. Most questions do not specify the population of other people.</p>
        <a class="more" href="#">+ READ MORE</a>
      </div>
    </article>
    <article class="card row2">
      <div class="img g2" role="img" aria-label="Photo of a presenter pointing at a board"></div>
      <div class="body">
        <span class="meta">28 Jan 2016 / Comment 2</span>
        <h3>Satisfaction with democracy</h3>
        <p>At the respondent level, the common variable indicates whether respondents are satisfied with the way their national democracy works.</p>
        <a class="more" href="#">+ READ MORE</a>
      </div>
    </article>
  </div>
</section>

<section class="panels">
  <article class="panel left">
    <h2>Support for democracy</h2>
    <p>At the respondent level, the common variable indicates when respondents find democracy preferable to other forms of government such as authoritarian or dictatorship governments. Responses indicating indifference and midpoints on scales were recoded as democracy being 'not always preferable'.</p>
    <a class="btn" href="#">Read more</a>
  </article>
  <article class="panel right">
    <h2>Perceived electoral integrity</h2>
    <p>At the respondent level, the common variable indicates when respondents generally approve electoral integrity in their country. Most questions refer to national or parliamentary elections, some do not specify the election type, and some specify presidential elections. Surveys use different wording when</p>
    <a class="btn" href="#">Read more</a>
  </article>
</section>

<footer class="footer">
  <a class="brand" href="#"><span class="dot"></span>KOVAL Polls</a>
  <p class="about">KOVAL Polls make it easier to work with multiple sources of public opinion data. It does so by formatting variables for consistency and merging datasets together. The current merged dataset includes millions of respondents, covers most countries in the world and extends back decades. This increased variation over time and space enables answering new research questions about the public.</p>
  <div class="subscribe"><span class="field">Enter your email</span><a class="btn" href="#">Send</a></div>
  <nav class="foot-nav">
    <a href="#">HOME</a><a href="#">ABOUT US</a><a href="#">SERVICES</a><a href="#">TESTIMONIALS</a><a href="#">BLOG</a><a href="#">CONTACT US</a>
  </nav>
  <div class="legal">
    <p>Copyright © 2018 <b>KOVAL POLLS</b> All Rights Reserved.</p>
    <div class="social"><span></span><span></span><span></span><span></span><span></span><span></span></div>
  </div>
</footer>

</body>
</html>
```